Design a web site for my business - Brellan Coatworks Mackaby.

We are a family business that handles design, fabrication and installation of powder coated aluminum, stainless steel and glass products. Including handrails, privacy slat screens, electric gates and pool fencing. We are based in the Whitsundays in North Queensland and service an area from Airlie Beach to Townsville.

Target Market(s)

Domestic and commercial

Industry/Entity Type

fabrication - manufacturing

Coding

Coded - Design and coding required

Number of Pages Required

5+ page

Colors
0054AA
0677BA
7BADD7
CADEEF
E8F1F8

Requirements
Must have
• photo galleries, contact page, one page for privacy screens, balustrades, glass fencing, stainless steel handrail, powder coated aluminium handrails and pool fencing

```html
<!DOCTYPE html>
<html lang="en">
<head>
<meta charset="utf-8">
<title>Brellan Coatworks Mackaby — Fabricated for the coast</title>
<link rel="stylesheet" href="https://fonts.googleapis.com/css2?family=Archivo:wght@400;500;600;700;800;900&family=IBM+Plex+Mono:wght@400;500;600&display=swap">
<style>
:root{
  --navy:#0f2038;
  --navy-2:#132843;
  --blue:#0054AA;
  --blue-2:#0677BA;
  --blue-3:#7BADD7;
  --blue-4:#CADEEF;
  --blue-5:#E8F1F8;
  --sand:#f4f1ea;
  --white:#ffffff;
  --ink:#14233a;
  --muted:#5b6675;
  --line:#d9d4c8;
  --sans:"Archivo",Helvetica,Arial,sans-serif;
  --mono:"IBM Plex Mono",Menlo,monospace;
}
*{box-sizing:border-box;margin:0;padding:0}
html,body{width:1200px;height:4079px;overflow:hidden}
body{font-family:var(--sans);color:var(--ink);background:var(--white);position:relative}
.wrap{position:absolute;left:171px;width:858px}
section,header,footer{position:relative;width:1200px}
.mono{font-family:var(--mono)}
.label{font-family:var(--mono);font-size:9px;letter-spacing:.08em;color:var(--blue-2);text-transform:uppercase}
.h2{font-family:var(--sans);font-weight:900;font-size:27px;line-height:1.15;letter-spacing:.01em;text-transform:uppercase;color:var(--navy)}
.ph{display:block;width:100%;height:100%}

/* top bar */
.topbar{height:24px;background:var(--navy);color:var(--blue-4)}
.topbar .wrap{top:0;height:24px;display:flex;justify-content:space-between;align-items:center;font-family:var(--mono);font-size:9px;letter-spacing:.08em}
.topbar .tel{color:var(--white)}

/* nav */
.nav{height:74px;background:var(--sand);border-bottom:1px solid var(--line)}
.nav .wrap{top:0;height:74px;display:flex;align-items:center;justify-content:space-between}
.brand{display:flex;align-items:center;gap:7px;font-weight:700;font-size:11px;color:var(--navy);letter-spacing:.02em;text-transform:uppercase}
.brand i{width:10px;height:10px;background:var(--navy);display:block}
.menu{display:flex;align-items:center;gap:22px;font-family:var(--mono);font-size:10px;letter-spacing:.06em;color:var(--navy)}
.menu b{color:var(--blue-2);font-weight:500}
.btn{display:inline-flex;align-items:center;justify-content:center;font-family:var(--sans);font-weight:800;font-size:10px;letter-spacing:.04em;text-transform:uppercase}
.btn-blue{background:var(--blue);color:var(--white)}
.menu .btn{width:108px;height:28px;margin-left:6px}

/* hero */
.hero{height:559px;background:var(--sand)}
.hero-frame{position:absolute;left:171px;top:29px;width:858px;height:490px;border:2px solid var(--navy);overflow:hidden}
.hero-photo{position:absolute;inset:0;background:linear-gradient(180deg,#4e7fb0 0%,#3d6f98 28%,#2d5675 52%,#1c3552 78%,#15263d 100%)}
.corner{position:absolute;width:20px;height:20px;border-color:var(--white);border-style:solid}
.corner.tl{left:14px;top:12px;border-width:2px 0 0 2px}
.corner.tr{right:14px;top:12px;border-width:2px 2px 0 0}
.fig{position:absolute;right:40px;top:16px;font-family:var(--mono);font-size:9px;letter-spacing:.08em;color:var(--white)}
.hero-copy{position:absolute;left:41px;top:116px;color:var(--white)}
.hero-copy .label{color:var(--blue-4);margin-bottom:14px}
.hero-copy h1{font-weight:900;font-size:44px;line-height:1;letter-spacing:.01em;text-transform:uppercase}
.hero-copy p{margin-top:26px;font-size:12px;line-height:21px;width:420px;color:#e8eef6}
.hero-btns{margin-top:20px;display:flex;gap:10px}
.hero-btns .btn{height:31px}
.hero-btns .btn-blue{width:152px}
.btn-ghost{width:134px;border:1.5px solid var(--white);color:var(--white)}
.stats{position:absolute;left:0;right:0;bottom:0;height:63px;display:grid;grid-template-columns:repeat(4,1fr);background:var(--sand);border-top:2px solid var(--navy)}
.stats div{padding:19px 20px 0;border-right:2px solid var(--navy)}
.stats div:last-child{border-right:0}
.stats span{display:block;font-family:var(--mono);font-size:8px;color:var(--blue-2)}
.stats strong{display:block;margin-top:3px;font-size:12px;font-weight:800;text-transform:uppercase;color:var(--navy)}

/* about */
.about{height:369px;background:var(--white);border-bottom:1px solid var(--line)}
.about .label{position:absolute;left:171px;top:63px}
.about-stat{position:absolute;left:171px;top:84px;height:78px;border-left:2px solid var(--navy);padding-left:16px}
.about-stat .big{font-weight:900;font-size:42px;line-height:1;color:var(--blue-4)}
.about-stat .small{margin-top:10px;font-family:var(--mono);font-size:8px;line-height:13px;color:var(--muted);letter-spacing:.04em}
.about-copy{position:absolute;left:461px;top:74px;width:460px}
.about-copy p{font-size:11.5px;line-height:21px;color:var(--muted);margin-top:20px}
.about-copy p+p{margin-top:16px}
.link{display:inline-block;margin-top:18px;font-weight:800;font-size:10px;text-transform:uppercase;color:var(--blue);border-bottom:1.5px solid var(--blue);padding-bottom:2px}

/* products */
.products{height:989px;background:var(--sand)}
.products .label{position:absolute;left:171px;top:61px}
.products .h2{position:absolute;left:171px;top:79px}
.products .intro{position:absolute;left:742px;top:73px;width:287px;font-size:10.5px;line-height:18px;color:var(--muted)}
.grid{position:absolute;left:171px;top:139px;width:858px;display:grid;grid-template-columns:repeat(3,1fr);grid-auto-rows:259px;border:1.5px solid var(--navy);background:var(--white)}
.card{border-right:1px solid var(--line);border-bottom:1px solid var(--line);position:relative;background:var(--white)}
.card:nth-child(3n){border-right:0}
.card .img{height:150px;position:relative}
.tag{position:absolute;left:8px;top:7px;background:var(--navy);color:var(--white);font-family:var(--mono);font-size:8px;padding:3px 6px;letter-spacing:.05em}
.card .body{padding:16px 18px 0}
.card h3{font-weight:800;font-size:13.5px;line-height:16px;text-transform:uppercase;color:var(--navy)}
.card p{margin-top:7px;font-size:9.5px;line-height:16px;color:var(--muted)}
.card .enq{margin-top:10px;font-family:var(--mono);font-size:8.5px;color:var(--blue-2);letter-spacing:.06em}
.card-cta{grid-column:span 2;background:var(--navy);color:var(--white);display:flex;align-items:center;padding-left:30px;gap:18px}
.card-cta .q{font-weight:900;font-size:30px;color:var(--blue-3)}
.card-cta h3{font-weight:800;font-size:14px;text-transform:uppercase}
.card-cta p{margin-top:6px;font-size:9.5px;line-height:16px;color:var(--blue-4);width:320px}
.card-cta .enq{margin-top:6px;font-family:var(--mono);font-size:8.5px;letter-spacing:.06em}

/* process */
.process{height:399px;background:var(--navy)}
.process .label{position:absolute;left:171px;top:65px;color:var(--blue-3)}
.process .h2{position:absolute;left:171px;top:84px;color:var(--white)}
.steps{position:absolute;left:171px;top:154px;width:858px;height:182px;display:grid;grid-template-columns:repeat(3,1fr);border:1px solid #35507a}
.steps div{padding:26px 23px 0;border-right:1px solid #35507a}
.steps div:last-child{border-right:0}
.steps .n{font-family:var(--mono);font-size:30px;font-weight:500;color:var(--blue-2);line-height:1}
.steps h3{margin-top:14px;font-weight:800;font-size:14px;text-transform:uppercase;color:var(--white)}
.steps p{margin-top:12px;font-size:9.5px;line-height:17px;color:var(--blue-4)}

/* gallery */
.gallery{height:522px;background:var(--white);border-bottom:1px solid var(--line)}
.gallery .label{position:absolute;left:171px;top:68px}
.gallery .h2{position:absolute;left:171px;top:87px}
.gallery .view{position:absolute;right:171px;top:101px;font-family:var(--mono);font-size:9px;color:var(--blue);letter-spacing:.06em;border-bottom:1px solid var(--blue);padding-bottom:2px}
.g-grid{position:absolute;left:171px;top:139px;width:858px;height:317px;display:grid;grid-template-columns:429px 214px 1fr;grid-template-rows:159px 1fr;border:1.5px solid var(--navy)}
.g-item{position:relative;border-left:1px solid var(--white);border-bottom:1px solid var(--white)}
.g-item.big{grid-row:span 2;border-left:0}
.cap{position:absolute;left:0;bottom:0;background:var(--navy);color:var(--white);font-family:var(--mono);font-size:8px;letter-spacing:.08em;padding:6px 10px}

/* coverage */
.coverage{height:475px;background:var(--sand)}
.coverage .label{position:absolute;left:171px;top:59px}
.coverage .h2{position:absolute;left:171px;top:89px;line-height:30px}
.coverage .intro{position:absolute;left:171px;top:158px;width:410px;font-size:11px;line-height:21px;color:var(--muted)}
.areas{position:absolute;left:171px;top:211px;width:408px;border:1.5px solid var(--navy);background:var(--white)}
.areas li{list-style:none;height:29px;display:flex;align-items:center;justify-content:space-between;padding:0 13px;border-bottom:1px solid var(--line);font-weight:800;font-size:10.5px;text-transform:uppercase;color:var(--navy)}
.areas li:last-child{border-bottom:0}
.areas li span{font-family:var(--mono);font-weight:400;font-size:8px;color:var(--blue-2);letter-spacing:.05em}
.map{position:absolute;left:620px;top:95px;width:409px;height:282px;border:2px solid var(--navy);background:var(--white);overflow:hidden}
.map .ph{height:232px;margin-top:48px}

/* quote */
.quote{height:417px;background:var(--blue);color:var(--white)}
.quote .label{position:absolute;left:171px;top:106px;color:var(--blue-4)}
.quote h2{position:absolute;left:171px;top:124px;font-weight:900;font-size:31px;line-height:32px;text-transform:uppercase}
.quote .intro{position:absolute;left:171px;top:206px;width:330px;font-size:11px;line-height:20px;color:var(--blue-5)}
.contact{position:absolute;left:171px;top:255px;font-family:var(--mono);font-size:10px;line-height:21px;font-weight:600;letter-spacing:.04em}
.form{position:absolute;left:662px;top:57px;width:367px;height:300px;background:var(--white);border:2px solid var(--navy);padding:22px 23px}
.form h3{font-weight:900;font-size:16px;text-transform:uppercase;color:var(--navy)}
.field{margin-top:10px;height:32px;border:1.5px solid var(--navy);display:flex;align-items:center;padding:0 10px;font-size:9.5px;color:var(--muted);justify-content:space-between}
.field.first{margin-top:14px}
.field.area{height:57px;align-items:flex-start;padding-top:9px}
.form .send{margin-top:10px;height:32px;width:100%;background:var(--navy);color:var(--white)}

/* footer */
.footer{height:251px;background:var(--navy);color:var(--blue-4)}
.footer .brand{position:absolute;left:171px;top:34px;color:var(--white)}
.footer .brand i{background:var(--white)}
.footer .about-f{position:absolute;left:171px;top:90px;width:240px;font-size:9.5px;line-height:16px;color:#9fb1c8}
.fcol{position:absolute;top:34px}
.fcol h4{font-family:var(--mono);font-size:9px;letter-spacing:.08em;color:var(--white);font-weight:500;margin-bottom:8px}
.fcol li{list-style:none;font-size:9.5px;line-height:19px;color:#9fb1c8}
.fbar{position:absolute;left:171px;width:858px;top:204px;border-top:1px solid #2b4263;padding-top:14px;display:flex;justify-content:space-between;font-family:var(--mono);font-size:8px;letter-spacing:.08em;color:#9fb1c8}
</style>
</head>
<body>

<header class="topbar">
  <div class="wrap"><span>WHITSUNDAYS QLD // AIRLIE BEACH — TOWNSVILLE</span><span class="tel">TEL (07) 4900 1234</span></div>
</header>

<nav class="nav">
  <div class="wrap">
    <div class="brand"><i></i>Brellan Coatworks Mackaby</div>
    <div class="menu">
      <span><b>01/</b> PRODUCTS</span>
      <span><b>02/</b> GALLERY</span>
      <span><b>03/</b> SERVICE AREA</span>
      <span class="btn btn-blue">Get a quote</span>
    </div>
  </div>
</nav>

<section class="hero">
  <div class="hero-frame">
    <div class="hero-photo" role="img" aria-label="Photo of a foreshore handrail at Airlie Beach with palm trees, rocks and calm water"></div>
    <span class="corner tl"></span><span class="corner tr"></span>
    <div class="fig">FIG. 01 — FORESHORE HANDRAIL, AIRLIE BEACH</div>
    <div class="hero-copy">
      <div class="label">MATERIALS · ALUMINIUM · STAINLESS STEEL · GLASS</div>
      <h1>Fabricated<br>for the coast.<br>Built to spec.</h1>
      <p>Handrails, balustrades, privacy screens, pool fencing and electric gates — design, fabrication and installation, all under one Whitsundays roof.</p>
      <div class="hero-btns"><span class="btn btn-blue">Request a quote</span><span class="btn btn-ghost">Our products</span></div>
    </div>
    <div class="stats">
      <div><span>01</span><strong>Family owned</strong></div>
      <div><span>02</span><strong>Marine grade</strong></div>
      <div><span>03</span><strong>Fully compliant</strong></div>
      <div><span>04</span><strong>Wide coverage</strong></div>
    </div>
  </div>
</section>

<section class="about">
  <div class="label">§ 01 — ABOUT</div>
  <div class="about-stat">
    <div class="big">100%</div>
    <div class="small">DESIGNED · FABRICATED<br>INSTALLED IN-HOUSE</div>
  </div>
  <div class="about-copy">
    <h2 class="h2">One team, from first<br>sketch to final install</h2>
    <p>We're a Whitsundays family business handling the whole job in-house — measure and design, fabrication in our workshop, powder coating, and installation on site. No middlemen, no handballing. Marine-grade materials chosen for North Queensland's salt, sun and cyclone conditions.</p>
    <p>From a single pool fence to full commercial foreshore projects, we work with homeowners, builders and councils from Airlie Beach to Townsville.</p>
    <span class="link">Talk to us about your project →</span>
  </div>
</section>

<section class="products">
  <div class="label">§ 02 — CATALOGUE</div>
  <h2 class="h2">Products &amp; services</h2>
  <p class="intro">Every product custom measured, fabricated to Australian Standards and powder coated in your choice of colour.</p>
  <div class="grid">
    <div class="card"><div class="img"><svg class="ph" role="img" aria-label="Photo of powder coated aluminium handrail along a rocky waterfront"><defs><linearGradient id="p1" x1="0" y1="0" x2="0" y2="1"><stop offset="0" stop-color="#7fa7cf"/><stop offset=".55" stop-color="#5a7f8c"/><stop offset="1" stop-color="#6a4e3a"/></linearGradient></defs><rect width="100%" height="100%" fill="url(#p1)"/></svg><span class="tag">SPEC 01</span></div>
      <div class="body"><h3>Powder coated aluminium handrails</h3><p>Durable, low-maintenance handrails in any powder coat colour — built for coastal conditions.</p><div class="enq">ENQUIRE →</div></div></div>
    <div class="card"><div class="img"><svg class="ph" role="img" aria-label="Photo of stainless steel wire handrail beside a timber boardwalk"><defs><linearGradient id="p2" x1="0" y1="0" x2="0" y2="1"><stop offset="0" stop-color="#8ea1a8"/><stop offset=".5" stop-color="#6f7a6a"/><stop offset="1" stop-color="#7b5a45"/></linearGradient></defs><rect width="100%" height="100%" fill="url(#p2)"/></svg><span class="tag">SPEC 02</span></div>
      <div class="body"><h3>Stainless steel handrails</h3><p>Marine-grade 316 stainless handrails and wire balustrades, polished or brushed finish.</p><div class="enq">ENQUIRE →</div></div></div>
    <div class="card"><div class="img"><svg class="ph" role="img" aria-label="Photo of glass balustrade on an elevated timber deck"><defs><linearGradient id="p3" x1="0" y1="0" x2="0" y2="1"><stop offset="0" stop-color="#4a3a2e"/><stop offset=".5" stop-color="#8c7a68"/><stop offset="1" stop-color="#b9bcb8"/></linearGradient></defs><rect width="100%" height="100%" fill="url(#p3)"/></svg><span class="tag">SPEC 03</span></div>
      <div class="body"><h3>Balustrades</h3><p>Glass, stainless and aluminium balustrades for decks, stairs and balconies — compliant to AS1170.</p><div class="enq">ENQUIRE →</div></div></div>
    <div class="card"><div class="img"><svg class="ph" role="img" aria-label="Photo of frameless glass fencing beside tropical garden"><defs><linearGradient id="p4" x1="0" y1="0" x2="0" y2="1"><stop offset="0" stop-color="#3f5a3a"/><stop offset=".6" stop-color="#7f8f7a"/><stop offset="1" stop-color="#b8b6ab"/></linearGradient></defs><rect width="100%" height="100%" fill="url(#p4)"/></svg><span class="tag">SPEC 04</span></div>
      <div class="body"><h3>Glass fencing</h3><p>Frameless and semi-frameless glass fencing that keeps your view exactly where it should be.</p><div class="enq">ENQUIRE →</div></div></div>
    <div class="card"><div class="img"><svg class="ph" role="img" aria-label="Photo of cream aluminium privacy slat screen and gate"><defs><linearGradient id="p5" x1="0" y1="0" x2="0" y2="1"><stop offset="0" stop-color="#9fb3c4"/><stop offset=".35" stop-color="#d9d4c6"/><stop offset="1" stop-color="#b9b2a3"/></linearGradient></defs><rect width="100%" height="100%" fill="url(#p5)"/></svg><span class="tag">SPEC 05</span></div>
      <div class="body"><h3>Privacy slat screens</h3><p>Custom aluminium slat screens and gates for privacy, pool equipment, bins and courtyards.</p><div class="enq">ENQUIRE →</div></div></div>
    <div class="card"><div class="img"><svg class="ph" role="img" aria-label="Photo of glass pool fencing with palms behind"><defs><linearGradient id="p6" x1="0" y1="0" x2="0" y2="1"><stop offset="0" stop-color="#445e3d"/><stop offset=".6" stop-color="#84947e"/><stop offset="1" stop-color="#bdbab0"/></linearGradient></defs><rect width="100%" height="100%" fill="url(#p6)"/></svg><span class="tag">SPEC 06</span></div>
      <div class="body"><h3>Pool fencing</h3><p>Compliant aluminium and glass pool fencing, certified to QLD pool safety standards.</p><div class="enq">ENQUIRE →</div></div></div>
    <div class="card"><div class="img"><svg class="ph" role="img" aria-label="Photo of cream aluminium slat electric gate"><defs><linearGradient id="p7" x1="0" y1="0" x2="0" y2="1"><stop offset="0" stop-color="#8fb0cf"/><stop offset=".35" stop-color="#d6d0c2"/><stop offset="1" stop-color="#aea693"/></linearGradient></defs><rect width="100%" height="100%" fill="url(#p7)"/></svg><span class="tag">SPEC 07</span></div>
      <div class="body"><h3>Electric gates</h3><p>Automated sliding and swing gates with remote and keypad access, fabricated to suit your entry.</p><div class="enq">ENQUIRE →</div></div></div>
    <div class="card-cta">
      <span class="q">?</span>
      <div><h3>Don't see what you need?</h3><p>Every job we take on is custom measured and fabricated — tell us what you're after and we'll design it to fit.</p><div class="enq">ENQUIRE →</div></div>
    </div>
  </div>
</section>

<section class="process">
  <div class="label">§ 03 — PROCESS</div>
  <h2 class="h2">Design. Fabricate. Install.</h2>
  <div class="steps">
    <div><div class="n">01</div><h3>Design &amp; measure</h3><p>We visit your site, measure up and design the job with you — materials, finish and powder coat colour.</p></div>
    <div><div class="n">02</div><h3>Fabricate &amp; coat</h3><p>Everything is fabricated in our Whitsundays workshop and powder coated for a finish that survives salt and sun.</p></div>
    <div><div class="n">03</div><h3>Install</h3><p>Our own installers fit the job on site, on schedule — and leave it certified, clean and ready to use.</p></div>
  </div>
</section>

<section class="gallery">
  <div class="label">§ 04 — ARCHIVE</div>
  <h2 class="h2">From the gallery</h2>
  <span class="view">VIEW FULL GALLERY →</span>
  <div class="g-grid">
    <div class="g-item big"><svg class="ph" role="img" aria-label="Photo of foreshore handrails along a rocky bay with a flowering tree"><defs><linearGradient id="g1" x1="0" y1="0" x2="0" y2="1"><stop offset="0" stop-color="#8fb1d6"/><stop offset=".45" stop-color="#5f8096"/><stop offset=".75" stop-color="#59636a"/><stop offset="1" stop-color="#7a5134"/></linearGradient></defs><rect width="100%" height="100%" fill="url(#g1)"/></svg><span class="cap">FIG. 01 — FORESHORE HANDRAILS</span></div>
    <div class="g-item"><svg class="ph" role="img" aria-label="Photo of glass fencing in a garden"><defs><linearGradient id="g2" x1="0" y1="0" x2="0" y2="1"><stop offset="0" stop-color="#465f3f"/><stop offset="1" stop-color="#aeb0a6"/></linearGradient></defs><rect width="100%" height="100%" fill="url(#g2)"/></svg><span class="cap">FIG. 02 — GLASS</span></div>
    <div class="g-item"><svg class="ph" role="img" aria-label="Photo of slat screens beside a house"><defs><linearGradient id="g3" x1="0" y1="0" x2="0" y2="1"><stop offset="0" stop-color="#94b4d2"/><stop offset=".4" stop-color="#d5cfc1"/><stop offset="1" stop-color="#a99f8b"/></linearGradient></defs><rect width="100%" height="100%" fill="url(#g3)"/></svg><span class="cap">FIG. 03 — SLAT SCREENS</span></div>
    <div class="g-item"><svg class="ph" role="img" aria-label="Photo of glass balustrade on a raised deck"><defs><linearGradient id="g4" x1="0" y1="0" x2="0" y2="1"><stop offset="0" stop-color="#433428"/><stop offset=".55" stop-color="#8a7968"/><stop offset="1" stop-color="#b7b9b4"/></linearGradient></defs><rect width="100%" height="100%" fill="url(#g4)"/></svg><span class="cap">FIG. 04 — BALUSTRADES</span></div>
    <div class="g-item"><svg class="ph" role="img" aria-label="Photo of handrails beside a boardwalk"><defs><linearGradient id="g5" x1="0" y1="0" x2="0" y2="1"><stop offset="0" stop-color="#8fa2a6"/><stop offset=".5" stop-color="#6c7865"/><stop offset="1" stop-color="#7c5b47"/></linearGradient></defs><rect width="100%" height="100%" fill="url(#g5)"/></svg><span class="cap">FIG. 05 — HANDRAILS</span></div>
  </div>
</section>

<section class="coverage">
  <div class="label">§ 05 — COVERAGE</div>
  <h2 class="h2">Airlie Beach to<br>Townsville</h2>
  <p class="intro">Based in the Whitsundays, we service residential and commercial projects across the North Queensland coast — including the islands.</p>
  <ul class="areas">
    <li>Airlie Beach<span>SERVICED</span></li>
    <li>Cannonvale<span>SERVICED</span></li>
    <li>Proserpine<span>SERVICED</span></li>
    <li>Bowen<span>SERVICED</span></li>
    <li>Ayr<span>SERVICED</span></li>
    <li>Townsville<span>SERVICED</span></li>
    <li>Whitsunday Islands<span>SERVICED</span></li>
  </ul>
  <div class="map"><svg class="ph" role="img" aria-label="Map of the North Queensland coast showing the route from Townsville to Airlie Beach"><defs><linearGradient id="m1" x1="0" y1="1" x2="1" y2="0"><stop offset="0" stop-color="#d9e6cf"/><stop offset=".55" stop-color="#cfe2d6"/><stop offset="1" stop-color="#a9d4ea"/></linearGradient></defs><rect width="100%" height="100%" fill="url(#m1)"/></svg></div>
</section>

<section class="quote">
  <div class="label">§ 06 — QUOTE REQUEST</div>
  <h2>Get a free<br>measure &amp; quote</h2>
  <p class="intro">Tell us about your project and we'll come to you. Most quotes turned around within a week.</p>
  <div class="contact">TEL — (07) 4900 1234<br>EMAIL — quotes@brellancoatworks.com.au<br>BASE — WHITSUNDAYS, NORTH QUEENSLAND</div>
  <div class="form">
    <h3>Request a quote</h3>
    <div class="field first">Your name</div>
    <div class="field">Phone</div>
    <div class="field">Powder coated aluminium handrails<svg width="8" height="5" viewBox="0 0 8 5"><path d="M1 1l3 3 3-3" fill="none" stroke="#14233a" stroke-width="1.2"/></svg></div>
    <div class="field area">Tell us about the project...</div>
    <span class="btn send">Send request</span>
  </div>
</section>

<footer class="footer">
  <div class="brand"><i></i>Brellan Coatworks Mackaby</div>
  <p class="about-f">Family owned design, fabrication and installation of powder coated aluminium, stainless steel and glass products in North Queensland.</p>
  <div class="fcol" style="left:530px">
    <h4>PRODUCTS</h4>
    <ul><li>Powder coated handrails</li><li>Stainless steel handrails</li><li>Balustrades</li><li>Glass fencing</li><li>Privacy screens</li><li>Pool fencing</li><li>Electric gates</li></ul>
  </div>
  <div class="fcol" style="left:796px">
    <h4>CONTACT</h4>
    <ul><li>(07) 4900 1234</li><li>quotes@brellancoatworks.com.au</li><li>Whitsundays QLD</li><li>Mon–Fri 7am – 4pm</li></ul>
  </div>
  <div class="fbar"><span>© 2026 BRELLAN COATWORKS MACKABY. ALL RIGHTS RESERVED.</span><span>QBCC LICENSED · FULLY INSURED</span></div>
</footer>

</body>
</html>
```